New design for Hunting and Fishing trophy website

This project is for a psd (no coding) landing page plus one additional page for our company. GlintMount makes laser cut hunting and fishing trophies using customer's photographs. We want customers to understand our product at a glance and know they can order online easily from their smartphone or computer.

There should be a clear call to action that encourages visitors to continue on and place an order.

The site should perform well on smartphones as well as computers.

I am attaching our latest concept website. Please use it only to get background on our company and to see what we are trying to communicate to the visitors. We came up with this design on our own but want something clearer and more effective and probably entirely different.

You can also visit our current (ugly and ineffective) site at www.glintmount-example.com to learn more about our company and product.

The second page is our Trailhead Circle which is for outfitters and guides to promote their business by making their customers' experience more memorable by ordering GlintMounts for them. I'm attaching a psd of a really bad website mock-up of the Guide Page (again, we're looking for something much nicer and less wordy).

I've uploaded a couple extra before and after photos, and another photo of a trophy room. Our goal is for customers to start their own trophy room using GlintMounts. You don't need to use this photo (but you can), it's blurry. It helps you understand what we are trying to accomplish.

Of course, this site should appeal to hunting and fishing customers. Please be creative and help us succeed in this new business.

Target Market(s)

Hunting and Fishing sportsmen/women and people giving gifts to fellow hunters/fishers

Industry/Entity Type

Hunting

Number of Pages Required

2 page

Requirements
Must have
• Hunting and fishing feel.
• Clear call to action (we want orders). Our site will be set up so they can upload their photo, choose their text, and check out all in a few steps (we'll do this part).
• Communicate that we use their photo, You may want to use before and after images like I've uploaded.
Nice to have
• Our logo is in the psd files I've uploaded. That's the only element that must be on the new page (in addition to our product of course), but we're open to other logo styles if you want to suggest something that fits better with your design. Colors should look nice with our logo.
• Fast loading site, fonts that load fast are best.
• Our visitors may have just taken a photo of a fish or deer they are really proud of, and we want them to know we're a more accurate and affordable alternative to taxidermy that they can order right now using the photo they just took.
Should not have
• Too much going on. Most hunters are calm, nature lovers, so probably no bright flashy colors and busy graphics.

```html
<!DOCTYPE html>
<html lang="en">
<head>
<meta charset="utf-8">
<title>GlintMount – Laser Cut Hunting &amp; Fishing Trophies</title>
<link href="https://fonts.googleapis.com/css2?family=Lato:wght@300;400;700;900&family=Playfair+Display:wght@700&display=swap" rel="stylesheet">
<style>
:root{
  --teal:#22c3cf;
  --teal-dark:#17a9b4;
  --ink:#2d2d2d;
  --muted:#6f6f6f;
  --line:#cfcfcf;
  --dark:#262626;
  --darker:#1d1d1d;
  --paper:#ffffff;
  --mist:#efefef;
}
*{margin:0;padding:0;box-sizing:border-box}
html,body{width:1200px;height:4749px;overflow:hidden}
body{font-family:"Lato",Arial,sans-serif;color:var(--ink);background:var(--paper);position:relative}
section,header,footer{position:absolute;left:0;width:1200px;overflow:hidden}
.abs{position:absolute}
.teal-btn{position:absolute;background:var(--teal);color:#fff;font-weight:700;text-align:center;border-radius:3px}

/* header */
.site-header{top:0;height:117px;background:#fff}
.care{left:127px;top:14px;font-size:13px;color:var(--muted)}
.logo{left:127px;top:56px;font-size:36px;font-weight:400;color:var(--teal);letter-spacing:-.5px}
.cart{left:862px;top:12px;width:92px;height:24px;border:1px solid var(--line);font-size:11px;color:var(--muted);line-height:22px;text-align:center}
.social{top:17px;width:12px;height:12px;border-radius:50%;background:#bdbdbd}
.nav{top:70px;left:555px;display:flex;gap:28px;font-size:13px;font-weight:700;color:#555;align-items:center}
.nav .active{color:var(--teal)}
.nav .order{background:var(--teal);color:#fff;padding:7px 10px}

/* hero */
.hero{top:117px;height:473px;background:linear-gradient(100deg,#4a2e1d 0%,#7a5233 40%,#8d6a4b 70%,#5d3e28 100%)}
.hero-title{left:127px;top:70px;width:420px;font-family:"Playfair Display",Georgia,serif;font-size:40px;line-height:46px;color:#fff;letter-spacing:1px;text-transform:uppercase}
.hero-text{left:127px;top:183px;width:330px;font-size:13px;line-height:19px;color:#f2e8de}
.hero .teal-btn{left:127px;top:236px;width:118px;height:36px;line-height:36px;font-size:15px}
.trophy{border-radius:4px}

/* section headings */
.sec-head{position:absolute;left:0;width:1200px}
.sec-head h2{position:absolute;right:665px;text-align:right;font-size:48px;line-height:52px;font-weight:900;color:var(--ink);text-transform:uppercase}
.sec-head h2 span{display:block;font-weight:300}
.sec-head .rule{position:absolute;left:560px;width:2px;height:112px;background:var(--line)}
.sec-head .under{position:absolute;right:665px;width:60px;height:2px;background:var(--line)}
.sec-head p{position:absolute;left:585px;width:380px;font-size:13px;line-height:19px;color:var(--muted)}
.light h2,.light p{color:#fff}
.light .rule,.light .under{background:rgba(255,255,255,.6)}

/* how we do */
.how{top:590px;height:490px;background:#fff}
.feature-line{left:127px;top:266px;width:946px;height:1px;background:var(--line)}
.feature-circle{width:114px;height:114px;border-radius:50%;border:2px solid var(--line);background:#fff;display:flex;align-items:center;justify-content:center}
.feature-circle.on{border-color:var(--teal)}
.feature-title{font-size:17px;line-height:21px;color:var(--ink)}
.feature-title.on{color:var(--teal)}
.feature-text{width:300px;font-size:13px;line-height:19px;color:var(--muted)}

/* about */
.about{top:1080px;height:533px;background:linear-gradient(90deg,#3a3a3a 0%,#2b2b2b 40%,#3f3a36 100%)}
.about-lead{left:460px;top:215px;width:620px;font-size:20px;line-height:28px;font-weight:700;color:#fff;text-transform:uppercase}
.about-text{left:460px;top:318px;width:620px;font-size:13px;line-height:19px;color:#e0e0e0}

/* works grid */
.works{top:1613px;height:889px;background:#fff}
.work-card{width:460px;height:294px}
.work-cap{right:18px;top:108px;width:160px;text-align:center}
.work-cap h3{font-size:17px;line-height:22px;font-weight:700;color:var(--ink);background:rgba(255,255,255,.85);padding:4px 6px;text-transform:uppercase}
.work-cap p{font-size:12px;line-height:16px;color:var(--ink);font-weight:700;margin-top:6px}
.work-icons{left:120px;top:170px;display:flex;gap:18px}
.work-icons span{width:40px;height:40px;border-radius:50%;background:#fff;display:flex;align-items:center;justify-content:center}

/* blog */
.blog{top:2502px;height:657px;background:linear-gradient(90deg,#5b5d60 0%,#8a8d90 45%,#6a6c6f 100%)}
.post{width:407px;height:203px;background:#fff;padding:22px 20px}
.post h3{font-size:16px;line-height:20px;font-weight:700;text-transform:uppercase;color:var(--ink)}
.post .author{font-size:13px;color:var(--muted);margin:10px 0 8px}
.post p{font-size:12px;line-height:18px;color:var(--muted)}
.date{width:58px;height:62px;background:var(--teal);color:#fff;font-size:13px;font-weight:700;text-align:center;padding-top:10px;line-height:18px}
.comments{width:58px;height:62px;background:var(--teal-dark);color:#fff;font-size:12px;text-align:center;padding-top:12px;line-height:16px}

/* testimonials */
.says{top:3159px;height:603px;background:#fff}
.testi-name{font-size:15px;color:var(--ink)}
.testi-role{font-size:12px;color:var(--muted);font-weight:700;margin:4px 0 8px}
.testi-text{font-size:12px;line-height:18px;color:var(--muted)}
.quote{font-size:60px;line-height:40px;color:#cfcfcf;font-family:Georgia,serif}
.dots{left:582px;top:546px;display:flex;gap:6px}
.dots span{width:9px;height:9px;border-radius:50%;background:#9aa}
.dots span.on{background:var(--teal)}

/* pricing */
.pricing{top:3762px;height:683px;background:var(--mist)}
.plan{color:#fff;text-align:center}
.plan .size{font-size:26px;margin-top:42px}
.plan .dim{font-size:17px;margin-top:4px}
.plan .price{font-size:34px;font-weight:700;margin-top:36px}
.plan ul{list-style:none;margin:40px 28px 0}
.plan li{font-size:12px;line-height:40px;border-top:1px solid rgba(255,255,255,.25)}
.plan li:last-child{border-bottom:1px solid rgba(255,255,255,.25)}
.plan .book{display:inline-block;margin-top:34px;background:var(--teal);color:#fff;font-size:13px;font-weight:700;padding:9px 20px;border-radius:3px}
.plan.featured .book{background:#fff;color:var(--ink)}

/* footer */
.site-footer{top:4445px;height:304px;background:var(--darker);color:#ddd}
.foot-logo{left:127px;top:36px;font-size:34px;color:var(--teal)}
.foot-contact{left:127px;top:100px;font-size:13px;line-height:21px;color:#cfcfcf;width:200px}
.foot-head{font-size:24px;color:#fff}
.recent{display:flex;gap:12px;margin-top:16px}
.recent .thumb{width:78px;height:52px}
.recent h4{font-size:13px;color:#fff}
.recent p{font-size:12px;line-height:15px;color:#bbb}
.links{list-style:none;margin-top:14px}
.links li{font-size:12px;line-height:24px;color:#ddd;text-transform:uppercase}
.links li::before{content:"";display:inline-block;width:5px;height:5px;background:#ddd;margin-right:10px;vertical-align:middle}
.news-input{width:220px;height:32px;background:#fff;color:#777;font-size:12px;line-height:32px;padding-left:10px;margin-top:16px}
.news-btn{display:inline-block;margin-top:12px;background:var(--teal);color:#fff;font-size:12px;padding:7px 14px}
</style>
</head>
<body>

<header class="site-header">
  <div class="abs care">Costumer Care : (555) 014 2290</div>
  <div class="abs logo">GlintMount</div>
  <div class="abs cart">Add to Cart</div>
  <span class="abs social" style="left:972px"></span>
  <span class="abs social" style="left:992px"></span>
  <span class="abs social" style="left:1012px"></span>
  <span class="abs social" style="left:1032px"></span>
  <nav class="abs nav">
    <span class="active">HOME</span><span>ABOUT US</span><span>TRAILHEAD CIRCLE</span><span>CONTACT US</span><span>FAQ</span><span class="order">ONLINE ORDER</span>
  </nav>
</header>

<section class="hero">
  <h1 class="abs hero-title">We create a best trophy</h1>
  <p class="abs hero-text">There are many variations of passages of Lorem Ipsum available, but the majority have suffered alteration in so</p>
  <a class="teal-btn">Order Now</a>
  <div class="abs trophy" role="img" aria-label="Laser cut trophy of a hunter in orange vest with a deer" style="left:560px;top:40px;width:200px;height:330px;background:linear-gradient(180deg,#c96a3a,#3b2a1f)"></div>
  <div class="abs trophy" role="img" aria-label="Laser cut trophy of an angler holding a large fish" style="left:800px;top:60px;width:230px;height:320px;background:linear-gradient(180deg,#6b86a6,#2f3e57)"></div>
</section>

<section class="how">
  <div class="sec-head" style="top:30px">
    <h2 style="top:8px">How<span>we do ?</span></h2>
    <div class="under" style="top:126px"></div>
    <div class="rule" style="top:6px"></div>
    <p style="top:14px">Lorem Ipsum is simply dummy text of the printing and typesetting industry. Lorem Ipsum has been the industry's standard dummy text ever since the when an unknown printer took a galley of type and scrambled it to make a type specimen book. It has survived not only</p>
  </div>
  <div class="abs feature-line"></div>
  <div class="abs feature-title" style="left:122px;top:272px">Intricate<br>Interior Cuts</div>
  <div class="abs feature-circle" style="left:305px;top:209px">
    <svg width="44" height="44" viewBox="0 0 44 44" fill="none" stroke="#555" stroke-width="3"><path d="M22 6 L32 22 M32 22 L26 22 M12 30 L22 38 M22 38 L22 32 M34 30 L16 30 M16 30 L20 26"/><path d="M14 24 L20 12"/></svg>
  </div>
  <div class="abs feature-title on" style="left:450px;top:272px">Pricision Lasercut<br>Buy Degreed Artists</div>
  <div class="abs feature-circle on" style="left:633px;top:209px">
    <svg width="46" height="46" viewBox="0 0 46 46" fill="none" stroke="#22c3cf" stroke-width="3"><path d="M10 20 A14 14 0 0 1 35 15"/><path d="M35 7 V15 H27"/><path d="M36 26 A14 14 0 0 1 11 31"/><path d="M11 39 V31 H19"/></svg>
  </div>
  <div class="abs feature-title" style="left:775px;top:272px">Superthick<br>protective Coating</div>
  <div class="abs feature-circle" style="left:960px;top:209px">
    <svg width="44" height="44" viewBox="0 0 44 44" fill="none" stroke="#555" stroke-width="3"><circle cx="22" cy="22" r="16"/><circle cx="22" cy="22" r="9"/><circle cx="22" cy="22" r="2" fill="#555"/></svg>
  </div>
  <p class="abs feature-text" style="left:122px;top:352px">There are many variations of passages of Lorem Ipsum available, but the majority have suffered alteration in some form, by injected humour, or rando</p>
  <p class="abs feature-text" style="left:450px;top:352px">There are many variations of passages of Lorem Ipsum available, but the majority have suffered alteration in some form, by injected humour, or rando</p>
  <p class="abs feature-text" style="left:775px;top:352px">There are many variations of passages of Lorem Ipsum available, but the majority have suffered alteration in some form, by injected humour, or rando</p>
</section>

<section class="about">
  <div class="abs" role="img" aria-label="Blurred team photo behind the about section" style="left:0;top:0;width:420px;height:533px;background:linear-gradient(90deg,#1f1f1f,#4a4440)"></div>
  <div class="sec-head light" style="top:70px">
    <h2 style="top:8px">About<span>our self</span></h2>
    <div class="under" style="top:126px"></div>
    <div class="rule" style="top:6px"></div>
    <p style="top:14px">Lorem Ipsum is simply dummy text of the printing and typesetting industry. Lorem Ipsum has been the industry's standard dummy text ever since the when an unknown printer took a galley of type and scrambled it to make a type specimen book. It has survived not only</p>
  </div>
  <p class="abs about-lead">Lorem Ipsum is simply dummy text of the printing and typesetting industry. Lorem Ipsum has been the industry's standard dummy text ever since the 1500s.</p>
  <p class="abs about-text">Lorem Ipsum is simply dummy text of the printing and typesetting industry. Lorem Ipsum has been the industry's standard dummy text ever since the 1500s, when an unknown printer took a galley of type and scrambled it to make a type specimen book. It has survived not only five centuries, but also the leap into electronic typesetting, remaining unchanged.</p>
</section>

<section class="works">
  <div class="sec-head" style="top:50px">
    <h2 style="top:8px">Our<span>works</span></h2>
    <div class="under" style="top:126px"></div>
    <div class="rule" style="top:6px"></div>
    <p style="top:14px">Lorem Ipsum is simply dummy text of the printing and typesetting industry. Lorem Ipsum has been the industry's standard dummy text ever since the when an unknown printer took a galley of type and scrambled it to make a type specimen book. It has survived not only</p>
  </div>
  <div class="abs work-card" role="img" aria-label="Trophy of a hunter with a deer on a light backdrop" style="left:127px;top:238px;background:linear-gradient(90deg,#d9d4cf,#f3f1ef)">
    <div class="abs work-cap"><h3>Lorem ipsum is simply dummy text of the</h3><p>Lorem Ipsum is simply dummy text of the printing and type-setting</p></div>
  </div>
  <div class="abs work-card" role="img" aria-label="Trophy of an angler with a fish on a grey backdrop" style="left:613px;top:238px;background:linear-gradient(90deg,#4a4a4a,#d8d8d8)">
    <div class="abs work-cap"><h3>Lorem ipsum is simply dummy text of the</h3><p>Lorem Ipsum is simply dummy text of the printing and type-setting</p></div>
  </div>
  <div class="abs work-card" role="img" aria-label="Engraved wooden hunting club plaque" style="left:127px;top:559px;background:linear-gradient(120deg,#111 0%,#3a2a16 35%,#c89a55 70%,#e0b878 100%)">
    <div class="abs work-cap"><h3>Lorem ipsum is simply dummy text of the</h3><p>Lorem Ipsum is simply dummy text of the printing and type-setting</p></div>
  </div>
  <div class="abs work-card" style="left:613px;top:559px;background:linear-gradient(120deg,#1c8f8b,#2fb3ad)" role="img" aria-label="Engraved plaque under a teal hover overlay">
    <div class="abs work-icons">
      <span><svg width="18" height="18" viewBox="0 0 18 18" fill="none" stroke="#333" stroke-width="2"><circle cx="7.5" cy="7.5" r="5"/><path d="M11 11 L16 16"/></svg></span>
      <span><svg width="18" height="18" viewBox="0 0 18 18" fill="none" stroke="#333" stroke-width="2"><path d="M7 11 L11 7 M8 4 L10 2 A3 3 0 0 1 16 8 L14 10 M10 14 L8 16 A3 3 0 0 1 2 10 L4 8"/></svg></span>
    </div>
    <div class="abs work-cap"><h3>Lorem ipsum is simply dummy text of the</h3><p>Lorem Ipsum is simply dummy text of the printing and type-setting</p></div>
  </div>
</section>

<section class="blog">
  <div class="sec-head light" style="top:30px">
    <h2 style="top:8px">Latest<span>from blog</span></h2>
    <div class="under" style="top:126px"></div>
    <div class="rule" style="top:6px"></div>
    <p style="top:14px">Lorem Ipsum is simply dummy text of the printing and typesetting industry. Lorem Ipsum has been the industry's standard dummy text ever since the when an unknown printer took a galley of type and scrambled it to make a type specimen book. It has survived not only</p>
  </div>
  <div class="abs" role="img" aria-label="Blog photo of a woman outdoors with a camera" style="left:206px;top:194px;width:381px;height:203px;background:linear-gradient(90deg,#4f7a3a,#b5c98c)">
    <div class="abs date" style="left:30px;top:80px">DEC 15<br>2014</div>
    <div class="abs comments" style="left:92px;top:80px">15<br>Comment</div>
  </div>
  <div class="abs post" style="left:587px;top:194px">
    <h3>Lorem ipsum is simply dummy text of</h3>
    <div class="author">&#9679; Evan Brooke</div>
    <p>There are many variations of passages of Lorem Ipsum available, but the majority have suffered alteration in some form, by injected humour, or randomised words which don't look even slightly believable. If you are going to use a passage</p>
  </div>
  <div class="abs post" style="left:206px;top:397px;width:381px">
    <h3>Lorem ipsum is simply dummy text of</h3>
    <div class="author">&#9679; Evan Brooke</div>
    <p>There are many variations of passages of Lorem Ipsum available, but the majority have suffered alteration in some form, by injected humour, or randomised words which don't look even slightly believable. If you are going to use a passage</p>
  </div>
  <div class="abs" role="img" aria-label="Blog photo of pink blossoms on a branch" style="left:587px;top:397px;width:407px;height:203px;background:linear-gradient(90deg,#f3eef0,#c2506e)">
    <div class="abs comments" style="left:260px;top:70px">15<br>Comment</div>
    <div class="abs date" style="left:322px;top:70px">DEC 15<br>2014</div>
  </div>
</section>

<section class="says">
  <div class="sec-head" style="top:50px">
    <h2 style="top:8px">What<span>people says</span></h2>
    <div class="under" style="top:126px"></div>
    <div class="rule" style="top:6px"></div>
    <p style="top:14px">Lorem Ipsum is simply dummy text of the printing and typesetting industry. Lorem Ipsum has been the industry's standard dummy text ever since the when an unknown printer took a galley of type and scrambled it to make a type specimen book. It has survived not only</p>
  </div>
  <svg class="abs" style="left:127px;top:254px" width="200" height="254" viewBox="0 0 200 254" role="img" aria-label="Portrait of a businesswoman on a teal ribbon">
    <rect x="30" y="0" width="150" height="230" fill="#d9d9d9"/>
    <polygon points="0,238 190,210 200,228 10,254" fill="#22c3cf"/>
  </svg>
  <div class="abs quote" style="left:338px;top:262px">&ldquo;</div>
  <div class="abs" style="left:422px;top:290px;width:165px">
    <div class="testi-name">Nora Fenwick</div>
    <div class="testi-role">Manager - ipsortrophy</div>
    <p class="testi-text">There are many variations of passages of Lorem Ipsum available, but the majority have suffered alteration in some form, by injected humour, or randomised words</p>
  </div>
  <div class="abs quote" style="left:548px;top:480px">&rdquo;</div>
  <svg class="abs" style="left:603px;top:254px" width="200" height="254" viewBox="0 0 200 254" role="img" aria-label="Portrait of a businessman on a teal ribbon">
    <rect x="30" y="0" width="150" height="230" fill="#d9d9d9"/>
    <polygon points="0,238 190,210 200,228 10,254" fill="#22c3cf"/>
  </svg>
  <div class="abs quote" style="left:815px;top:262px">&ldquo;</div>
  <div class="abs" style="left:863px;top:290px;width:210px">
    <div class="testi-name">Evan Brooke</div>
    <div class="testi-role">Manager - ipsortrophy</div>
    <p class="testi-text">There are many variations of passages of Lorem Ipsum available, but the majority have suffered alteration in some form, by injected humour, or randomised words</p>
  </div>
  <div class="abs quote" style="left:1035px;top:480px">&rdquo;</div>
  <div class="abs dots"><span></span><span class="on"></span><span></span></div>
</section>

<section class="pricing">
  <div class="sec-head" style="top:50px">
    <h2 style="top:8px">Our<span>works</span></h2>
    <div class="under" style="top:126px"></div>
    <div class="rule" style="top:6px"></div>
    <p style="top:14px">Lorem Ipsum is simply dummy text of the printing and typesetting industry. Lorem Ipsum has been the industry's standard dummy text ever since the when an unknown printer took a galley of type and scrambled it to make a type specimen book. It has survived not only</p>
  </div>
  <div class="abs plan" style="left:127px;top:223px;width:317px;height:397px;background:var(--dark);clip-path:polygon(0 4%,100% 0,100% 100%,0 100%)">
    <div class="size">Tropy size</div><div class="dim">5" x 7"</div><div class="price">$ 39.95</div>
    <ul><li>Lorem Ipsum text Form</li><li>Lorem Ipsum text Form</li><li>Lorem Ipsum text Form</li></ul>
    <span class="book">Book Now</span>
  </div>
  <div class="abs plan featured" style="left:454px;top:193px;width:292px;height:445px;background:var(--teal);clip-path:polygon(0 0,100% 3%,100% 100%,0 97%)">
    <div class="size">Tropy size</div><div class="dim">8" x 10"</div><div class="price">$44.95</div>
    <ul><li>Lorem Ipsum text Form</li><li>Lorem Ipsum text Form</li><li>Lorem Ipsum text Form</li></ul>
    <span class="book">Book Now</span>
  </div>
  <div class="abs plan" style="left:762px;top:223px;width:318px;height:397px;background:var(--dark);clip-path:polygon(0 0,100% 4%,100% 100%,0 100%)">
    <div class="size">Tropy size</div><div class="dim">5" x 7"</div><div class="price">$54.95</div>
    <ul><li>Lorem Ipsum text Form</li><li>Lorem Ipsum text Form</li><li>Lorem Ipsum text Form</li></ul>
    <span class="book">Book Now</span>
  </div>
</section>

<footer class="site-footer">
  <div class="abs foot-logo">GlintMount</div>
  <div class="abs foot-contact">Address : 12 Pine Ridge Road, Marsh Hollow 55190<br><br>Phone : 555-019-4417<br><br>Email : hello@glintmount-example.com</div>
  <div class="abs" style="left:368px;top:40px;width:230px">
    <div class="foot-head">Recent Post</div>
    <div class="recent"><div class="thumb" role="img" aria-label="Post thumbnail of a lakeside scene" style="background:linear-gradient(90deg,#2f4f6a,#7a9bb5)"></div><div><h4>Lorem ipsum text</h4><p>There are many varia tions of passages of</p></div></div>
    <div class="recent"><div class="thumb" role="img" aria-label="Post thumbnail of pink blossoms" style="background:linear-gradient(90deg,#f0e6ea,#c2506e)"></div><div><h4>Lorem ipsum text</h4><p>There are many varia tions of passages of</p></div></div>
  </div>
  <div class="abs" style="left:612px;top:40px">
    <div class="foot-head">Quick Links</div>
    <ul class="links"><li>Home</li><li>About us</li><li>Trailhead Circle</li><li>Contact us</li><li>FAQ</li></ul>
  </div>
  <div class="abs" style="left:857px;top:40px">
    <div class="foot-head">News Latters</div>
    <div class="news-input">Enter Email Address</div>
    <span class="news-btn">Subscribe</span>
  </div>
</footer>

</body>
</html>
```